Corporate flyer highlighting service offering for PR agency

A corporate flyer is needed for a new service offering that we are doing. The product name is HarborLeap it is a marketing and communications services offering for companies who are getting ready to sell their business. If we are really happy with the designer's work, there will be a great deal more projects. I am looking for a clean design with a few pops of color from my site. https://quillmarsh.partners. I am looking for a good design with data in sections. I am looking for a clean design that feels high-end but not cluttered. Please do not use images of people. Please see the following examples of types of designs I like.
https://www.tackboard.example/pin/839201746530918264/
https://www.tackboard.example/pin/402918375561029847/
https://assets.stockvale.example/corporate-flyer-template-KRTPMB
https://designbrook.example/item/corporate-flyer-template/81046395?s_rank=8
https://assets.stockvale.example/corporate-business-flyer-template-93PX7D

I had to place the project on hold as I choose the wrong type of project and did not get many designs as a result. I am reposting this with an updated brief.

Target Market(s)

Business sellers and brokers

Industry/Entity Type

Marketing for business sellers

Font styles to use
Sans Serif

Requirements
Must have
• Good quality design with content in sections. Clean and high end feeling is a must.
Should not have
• A lot of images of people.

```html
<!DOCTYPE html>
<html lang="en">
<head>
<meta charset="utf-8">
<title>HarborLeap – Quillmarsh Partners</title>
<link rel="stylesheet" href="https://fonts.googleapis.com/css2?family=Lato:ital,wght@0,400;0,700;1,700;1,900&family=Montserrat:wght@500;600&family=Raleway:wght@300&display=swap">
<style>
  :root {
    --brand-blue: #1665a9;
    --brand-blue-deep: #0f4f8c;
    --hex-blue: #2d8bd0;
    --accent-orange: #f7941d;
    --accent-green: #6aa444;
    --panel-grey: #f2f2f2;
    --ink: #2b2b2b;
    --ink-soft: #444;
    --white: #ffffff;
  }
  * { box-sizing: border-box; margin: 0; padding: 0; }
  html, body { width: 902px; height: 1200px; overflow: hidden; background: #e9e9e9; }
  .flyer { position: relative; width: 902px; height: 1200px; background: var(--white); font-family: "Lato", sans-serif; color: var(--ink); }

  .hero { position: absolute; left: 0; top: 0; width: 902px; height: 414px; }
  .hero svg { position: absolute; inset: 0; }
  .brand { position: absolute; left: 487px; top: 124px; width: 340px; display: flex; align-items: center; gap: 12px; justify-content: center; }
  .brand-mark { width: 20px; height: 20px; background: var(--accent-orange); flex: none; }
  .brand-name { font-family: "Montserrat", sans-serif; font-weight: 500; font-size: 22px; letter-spacing: 1px; color: var(--white); text-transform: uppercase; white-space: nowrap; }
  .product-name { position: absolute; left: 452px; top: 211px; width: 382px; text-align: right; font-family: "Montserrat", sans-serif; font-weight: 600; font-size: 46px; line-height: 56px; letter-spacing: 2px; color: var(--accent-orange); }
  .tagline { position: absolute; left: 353px; top: 280px; width: 472px; font-family: "Raleway", sans-serif; font-weight: 300; font-size: 24.5px; line-height: 28px; color: var(--white); }
  .tagline-line { display: block; white-space: nowrap; text-align: justify; text-align-last: justify; }
  .tagline-line:nth-child(1) { padding-left: 77px; }
  .tagline-line:nth-child(2) { padding-left: 51px; }
  .tagline-line:nth-child(3) { padding-left: 25px; }
  .tagline-line:nth-child(4) { text-align-last: left; }

  .services-column { position: absolute; left: 0; top: 414px; width: 437px; height: 751px; background: var(--panel-grey); }
  .intro { position: absolute; left: 42px; top: 50px; width: 368px; font-weight: 700; font-style: italic; font-size: 15px; line-height: 16.8px; text-align: justify; color: var(--ink); }
  .services-grid { position: absolute; left: 0; top: 180px; }
  .hex-label { font-family: "Lato", sans-serif; font-weight: 700; font-size: 16px; fill: var(--white); text-anchor: middle; }
  .closing { position: absolute; left: 42px; top: 652px; width: 386px; font-size: 12.6px; line-height: 15.4px; text-align: justify; color: var(--ink-soft); }

  .value-column { position: absolute; left: 472px; top: 464px; width: 379px; font-size: 14px; line-height: 16.8px; text-align: justify; color: var(--ink-soft); }
  .value-column p + p { margin-top: 17px; }

  .stat-accent { position: absolute; left: 557px; top: 661px; width: 305px; height: 458px; background: var(--accent-green); }
  .stat-card { position: absolute; left: 463px; top: 708px; width: 378px; height: 363px; background: var(--white); border: 3px solid #e2e2e2; box-shadow: 0 2px 6px rgba(0,0,0,0.25); padding: 50px 28px 0 26px; }
  .stat-quote { font-weight: 900; font-style: italic; font-size: 22.5px; line-height: 25.2px; text-align: justify; color: var(--ink); hyphens: manual; }

  .footer-band { position: absolute; left: 0; bottom: 0; width: 902px; height: 35px; background: var(--brand-blue); }
</style>
</head>
<body>
<main class="flyer">
  <header class="hero">
    <svg width="902" height="414" viewBox="0 0 902 414">
      <defs>
        <linearGradient id="hero-blue" x1="0" y1="0" x2="1" y2="1">
          <stop offset="0" stop-color="#1a6fb5"/>
          <stop offset="1" stop-color="#0f548f"/>
        </linearGradient>
        <linearGradient id="tower-sky" x1="0" y1="0" x2="0.6" y2="1">
          <stop offset="0" stop-color="#dbe9f5"/>
          <stop offset="0.35" stop-color="#9cc3e4"/>
          <stop offset="0.7" stop-color="#3f7fb8"/>
          <stop offset="1" stop-color="#1f4f7c"/>
        </linearGradient>
        <radialGradient id="sun-glint" cx="0.2" cy="0.1" r="0.45">
          <stop offset="0" stop-color="#f3b24a" stop-opacity="0.75"/>
          <stop offset="1" stop-color="#f3b24a" stop-opacity="0"/>
        </radialGradient>
      </defs>
      <rect width="902" height="414" fill="url(#hero-blue)"/>
      <g role="img" aria-label="Low-angle view of glass office towers rising into a bright blue sky">
        <polygon points="0,0 300,0 452,181 206,414 0,414" fill="url(#tower-sky)"/>
        <polygon points="0,0 300,0 452,181 206,414 0,414" fill="url(#sun-glint)"/>
      </g>
      <polyline points="312,-10 466,181 216,424" fill="none" stroke="#ffffff" stroke-width="24"/>
    </svg>
    <div class="brand"><span class="brand-mark"></span><span class="brand-name">Quillmarsh Partners</span></div>
    <h1 class="product-name">HARBORLEAP</h1>
    <p class="tagline">
      <span class="tagline-line">provides executives and business</span>
      <span class="tagline-line">owners with clear guidance to</span>
      <span class="tagline-line">unlock non-financial value ahead of</span>
      <span class="tagline-line">an exit.</span>
    </p>
  </header>

  <section class="services-column">
    <p class="intro">We design and implement communication and marketing strategies that deliver significant increases in brand awareness, identify reputational risks, and enhance brand perception, helping owners and investors to realize premium values for their companies. We support owners and companies through:</p>

    <svg class="services-grid" width="437" height="460" viewBox="0 0 437 460">
      <g fill="var(--hex-blue)">
        <polygon points="76,78 120,5 208,5 252,78 208,151 120,151"/>
        <polygon points="219,151 263,78 351,78 395,151 351,224 263,224"/>
        <polygon points="76,229 120,156 208,156 252,229 208,302 120,302"/>
        <polygon points="219,302 263,229 351,229 395,302 351,375 263,375"/>
        <polygon points="76,375 120,302 208,302 252,375 208,448 120,448"/>
      </g>
      <g fill="none" stroke="#fff" stroke-width="2.2" stroke-linecap="round" stroke-linejoin="round">
        <rect x="148" y="24" width="20" height="30"/>
        <line x1="160" y1="38" x2="160" y2="41"/>
        <path d="M172 39 h10 m-4 -4 l4 4 l-4 4"/>
        <circle cx="262" cy="125" r="11"/>
        <circle cx="262" cy="168" r="11"/>
        <path d="M275 125 c15 0 15 21 30 21 M275 168 c15 0 15 -22 30 -22 M305 146 h8"/>
        <polygon points="313,140 323,146 313,152" fill="#fff"/>
        <circle cx="147" cy="188" r="4"/>
        <path d="M140 205 l7 -10 l7 10 M141 192 l-6 -6 M153 192 l6 -6"/>
        <rect x="160" y="182" width="22" height="22"/>
        <line x1="171" y1="182" x2="171" y2="204"/><line x1="160" y1="193" x2="182" y2="193"/>
        <circle cx="137" cy="213" r="3.5"/><circle cx="150" cy="213" r="3.5"/><circle cx="163" cy="213" r="3.5"/>
        <path d="M131 226 q6 -8 12 0 M144 226 q6 -8 12 0 M157 226 q6 -8 12 0"/>
        <path d="M278 273 q-14 0 -14 16 q0 10 14 10 q14 0 14 -10 q0 -16 -14 -16 z M272 266 h12 l-3 7 h-6 z"/>
        <path d="M293 260 v35 M288 265 l10 -10 M288 255 l10 10"/>
        <path d="M300 296 h16 M303 290 h12 M303 284 h12"/>
        <circle cx="164" cy="325" r="8"/>
        <path d="M150 352 q0 -16 14 -16 q14 0 14 16 z"/>
        <path d="M164 321 v8"/>
      </g>
      <text class="hex-label" x="164" y="101">COMPANY EXIT</text>
      <text class="hex-label" x="164" y="120">PREPARATION</text>
      <text class="hex-label" x="307" y="201">M&amp;A</text>
      <text class="hex-label" x="164" y="275">IPO</text>
      <text class="hex-label" x="307" y="326">SPINOFF/</text>
      <text class="hex-label" x="307" y="345">DIVESTITURE</text>
      <text class="hex-label" x="164" y="386">NEW</text>
      <text class="hex-label" x="164" y="405">LEADERSHIP/</text>
      <text class="hex-label" x="164" y="424">INVESTOR</text>
    </svg>

    <p class="closing">Few sellers would list their home without first inspecting, repairing broken items, and making updates to highlight the positive aspects --increasing appeal to buyers. However, countless business owners leave money on the table during corporate exits due to a lack of preparation.</p>
  </section>

  <section class="value-column">
    <p>A strong communication and marketing strategy can significantly increase the value of your business leading up to an exit. Buyers are looking to mitigate risk and unlock potential value as a catalyst for clear growth potential.</p>
    <p>Highlighting your company’s success in the marketplace, identifying, and mitigating reptation risks before buyers do, enhancing employee engagement, finding hidden opportunities to boost marketing KPIs and showcasing IP, data, and innovation, can make a significant difference in valuation.</p>
  </section>

  <div class="stat-accent"></div>
  <aside class="stat-card">
    <p class="stat-quote">US institutional investors believe that Investor Relations (IR) accounts for a total variance of 30% in a compa&shy;ny’s valuation – from a premium of 10% for “superb” IR to a discount of 20% for “poor” IR. ---Corvane Research Group, “Harnessing IR’s Power to Impact a Company’s Valu&shy;ation.”</p>
  </aside>

  <footer class="footer-band"></footer>
</main>
</body>
</html>
```